Brightmoor Partners Branding Revamp

We are a consulting company, looking for a way to display and promote our brand. We have 2 sides to the business- Brightmoor (financial) and Partners (cyber security). The financial side products relate to business necessities: card processing, website design/hosting/maintenance, VoIP phone systems. The cyber security side promotes a bundled package of 4 solutions: network vulnerability scan, dark web scan, anti-ransomeware/malware software, and image-level backups. We want people to understand that partnering with Brightmoor Partners gives them “Elevated Peace of Mind” (tagline). Current badge and logos uploaded.

Target Market(s)

Small businesses

Contact Information for Business Card

Lena Marwick, Vice President, lena@brightmoorpartners.example, 555-806-1937, www.brightmoorpartners.example

Requirements
Nice to have
• I do prefer the darker background for front and back

```html
<!DOCTYPE html>
<html lang="en">
<head>
<meta charset="utf-8">
<title>Brightmoor Partners – Business Card</title>
<link rel="stylesheet" href="https://fonts.googleapis.com/css2?family=Arimo:wght@700&display=swap">
<style>
  :root {
    --page: #ffffff;
    --card: #1f1b1c;
    --ink: #ffffff;
    --accent: #e3232b;
  }
  * { margin: 0; padding: 0; box-sizing: border-box; }
  html, body {
    width: 927px; height: 1200px; overflow: hidden;
    background: var(--page);
    font-family: "Arimo", Arial, sans-serif;
  }
  .sheet { position: relative; width: 927px; height: 1200px; }
  .card {
    position: absolute; left: 133px; width: 662px; height: 397px;
    background: var(--card); overflow: hidden;
  }
  .card--front { top: 134px; }
  .card--back { top: 671px; }

  .front-name {
    position: absolute; left: 0; right: 0; top: 150px;
    text-align: center; color: var(--ink);
    font-size: 26px; font-weight: 700; letter-spacing: 7px; line-height: 1.35;
    text-transform: uppercase;
  }

  .contact-block {
    position: absolute; right: 282px; top: 0; width: 380px; text-align: right;
  }
  .person-name {
    position: absolute; right: 0; top: 92px; white-space: nowrap;
    color: var(--ink); font-size: 36px; font-weight: 700; line-height: 1;
  }
  .name-rule {
    position: absolute; right: 0; top: 137px; width: 318px; height: 2.5px;
    background: var(--accent);
  }
  .person-title {
    position: absolute; right: -2px; top: 141px;
    color: var(--accent); font-size: 23px; font-weight: 700; line-height: 1.1;
  }
  .contact-list { list-style: none; }
  .contact-item {
    position: absolute; right: 0; height: 22px;
    display: flex; align-items: center; gap: 10px;
    color: var(--ink); font-size: 17px; font-weight: 700; white-space: nowrap;
  }
  .contact-item svg { width: 22px; height: 22px; flex: none; }
  .contact-item--email { top: 207px; }
  .contact-item--phone { top: 243px; }
  .contact-item--web { top: 276px; }

  .divider {
    position: absolute; left: 401px; top: 0; width: 10px; height: 100%;
    background: var(--accent);
  }
  .back-name {
    position: absolute; left: 411px; right: 0; top: 195px;
    text-align: center; color: var(--ink);
    font-size: 16px; font-weight: 700; letter-spacing: 5px; line-height: 1.4;
    text-transform: uppercase;
  }
</style>
</head>
<body>
<main class="sheet">
  <section class="card card--front" aria-label="Card front">
    <p class="front-name">Brightmoor<br>Partners</p>
  </section>

  <section class="card card--back" aria-label="Card back">
    <div class="contact-block">
      <h1 class="person-name">Lena Marwick</h1>
      <div class="name-rule"></div>
      <p class="person-title">Vice President</p>
      <ul class="contact-list">
        <li class="contact-item contact-item--email">
          <span>lena@brightmoorpartners.example</span>
          <svg viewBox="0 0 24 24" aria-hidden="true">
            <rect x="1" y="4" width="22" height="16" fill="var(--accent)"/>
            <path d="M1 4 L12 13 L23 4 M1 20 L9 11 M23 20 L15 11" stroke="var(--card)" stroke-width="1.6" fill="none"/>
          </svg>
        </li>
        <li class="contact-item contact-item--phone">
          <span>555-806-1937</span>
          <svg viewBox="0 0 24 24" aria-hidden="true">
            <path fill="var(--accent)" d="M6.6 2.5c.6-.5 1.4-.4 1.9.2l2.4 3.2c.4.6.4 1.4-.1 1.9L9.3 9.3c1.1 2.3 3 4.3 5.4 5.4l1.5-1.5c.5-.5 1.3-.6 1.9-.1l3.2 2.4c.6.5.7 1.3.2 1.9l-1.7 2.1c-.8 1-2.2 1.4-3.4.9C10.3 18.2 5.8 13.7 3.6 7.6c-.4-1.2 0-2.6.9-3.4z"/>
          </svg>
        </li>
        <li class="contact-item contact-item--web">
          <span>www.brightmoorpartners.example</span>
          <svg viewBox="0 0 24 24" aria-hidden="true">
            <circle cx="12" cy="12" r="11" fill="var(--accent)"/>
            <g stroke="var(--card)" stroke-width="1.4" fill="none">
              <ellipse cx="12" cy="12" rx="4.5" ry="11"/>
              <line x1="12" y1="1" x2="12" y2="23"/>
              <line x1="1" y1="12" x2="23" y2="12"/>
              <path d="M3 6.5h18M3 17.5h18"/>
            </g>
          </svg>
        </li>
      </ul>
    </div>
    <div class="divider"></div>
    <p class="back-name">Brightmoor<br>Partners</p>
  </section>
</main>
</body>
</html>
```